Maple Dental Centre Kelvona business cards and presentation folder

dental practice needing innovative black business cards for 2 different dentists witrh appointment details written at the back of the card for the patient.
name of dentists: Dr Priyanka R Valtenhoff B.D.S., M.P.H (Hons)
Dr. Tom Garvel B.D.S.

Target Market(s)

professioinal, working class

Industry/Entity Type

Dental Clinic

Contact Information for Business Card

Dr. Tom Garvel B.D.S.

Font styles to use
Sans Serif

Requirements
Must have
• Front side: logo
• dentist name
• phone number: 07- 5581 2943
• back side: appointment details: date, time,
• Address: 117C, 48 Harlow Street, Kelvona - 4871, Northvale
• Email: admin@mapledentalcentrekelvona.example.au
• Website: www.mapledentalcentre.example.au
• preferable logo colors
Nice to have
• classy look more pleasing

```html
<!DOCTYPE html>
<html lang="en">
<head>
<meta charset="utf-8">
<title>Maple Dental Centre Kelvona – Business Card</title>
<link rel="stylesheet" href="https://fonts.googleapis.com/css2?family=Marcellus&family=Arimo:wght@400&display=swap">
<style>
  :root {
    --bg: #dcdde0;
    --card-black: #0d0d0d;
    --card-white: #ffffff;
    --green: #a6d38a;
    --green-band: #b7dc9c;
    --green-text: #9fcf80;
    --ink: #1c1c1c;
    --white-text: #f2f2f2;
    --dots: #555555;
  }
  * { box-sizing: border-box; margin: 0; padding: 0; }
  html, body { width: 1200px; height: 1200px; overflow: hidden; }
  body { background: var(--bg); position: relative; font-family: "Marcellus", serif; }

  .card {
    position: absolute; left: 160px; width: 880px; height: 538px;
    overflow: hidden; box-shadow: 0 6px 18px rgba(0,0,0,.18);
  }
  .card--front { top: 40px; background: var(--card-black); }
  .card--back { top: 622px; background: var(--card-white); }

  .band { position: absolute; left: 0; right: 0; bottom: 0; background: var(--green-band); }
  .band-rule { position: absolute; left: 0; right: 0; height: 2px; background: var(--green); }

  .card--front .band { height: 70px; }
  .card--front .band-rule { bottom: 80px; }

  .brand-name {
    position: absolute; color: var(--green-text); font-family: "Marcellus", serif;
    text-transform: uppercase; letter-spacing: 2px; white-space: nowrap;
  }
  .card--front .brand-name { right: 60px; top: 130px; font-size: 34px; }

  .dentist-name { position: absolute; left: 60px; top: 230px; color: var(--green-text); font-size: 42px; }
  .dentist-credentials { position: absolute; left: 62px; top: 292px; color: var(--white-text); font-size: 26px; }

  .phone {
    position: absolute; right: 60px; top: 384px; color: var(--white-text);
    font-size: 28px; display: flex; align-items: center; gap: 14px;
  }
  .phone-icon { width: 30px; height: 30px; }

  .card--back .brand-name { left: 0; right: 0; top: 50px; text-align: center; font-size: 40px; }
  .brand-rule { position: absolute; left: 120px; right: 120px; top: 110px; height: 2px; background: var(--ink); }

  .appointments { position: absolute; left: 60px; right: 60px; top: 160px; }
  .appointment-row { display: flex; gap: 40px; margin-bottom: 34px; }
  .field { flex: 1; display: flex; align-items: flex-end; gap: 8px; color: var(--green-text); font-size: 24px; }
  .field-line { flex: 1; border-bottom: 2px dotted var(--dots); height: 20px; }

  .card--back .band { height: 130px; }
  .card--back .band-rule { bottom: 140px; }
  .contact {
    position: absolute; left: 0; right: 0; bottom: 0; height: 130px;
    display: flex; flex-direction: column; justify-content: center; align-items: center; gap: 10px;
    font-family: "Arimo", sans-serif; color: var(--ink);
  }
  .contact-address { font-size: 22px; }
  .contact-online { font-size: 20px; }
</style>
</head>
<body>
  <section class="card card--front" aria-label="Business card front">
    <div class="brand-name">Maple Dental Centre Kelvona</div>
    <div class="dentist-name">Dr Priyanka R Valtenhoff</div>
    <div class="dentist-credentials">B.D.S., M.P.H (Hons)</div>
    <div class="phone">
      <span>07- 5581 2943</span>
      <svg class="phone-icon" viewBox="0 0 30 30" aria-hidden="true">
        <circle cx="15" cy="15" r="14" fill="#a6d38a"/>
        <path d="M11 8c1 0 2 2.5 2 3.2 0 .8-1.3 1.3-1.1 2 .6 1.8 2.2 3.5 4 4.2.7.2 1.2-1.1 2-1.1.7 0 3.1 1 3.1 2 0 1.4-1.5 2.7-3 2.7-4.8 0-9.3-4.5-9.3-9.3C8.7 9.5 10 8 11 8z" fill="#0d0d0d"/>
      </svg>
    </div>
    <div class="band-rule"></div>
    <div class="band"></div>
  </section>

  <section class="card card--back" aria-label="Business card back">
    <div class="brand-name">Maple Dental Centre Kelvona</div>
    <div class="brand-rule"></div>
    <div class="appointments">
      <div class="appointment-row">
        <div class="field"><span>Date</span><span class="field-line"></span></div>
        <div class="field"><span>Time</span><span class="field-line"></span></div>
      </div>
      <div class="appointment-row">
        <div class="field"><span>Date</span><span class="field-line"></span></div>
        <div class="field"><span>Time</span><span class="field-line"></span></div>
      </div>
      <div class="appointment-row">
        <div class="field"><span>Date</span><span class="field-line"></span></div>
        <div class="field"><span>Time</span><span class="field-line"></span></div>
      </div>
    </div>
    <div class="band-rule"></div>
    <div class="band"></div>
    <div class="contact">
      <div class="contact-address">117C, 48 Harlow Street, Kelvona - 4871, Northvale</div>
      <div class="contact-online">admin@mapledentalcentrekelvona.example.au | www.mapledentalcentre.example.au</div>
    </div>
  </section>
</body>
</html>
```